Marcus Pellow Carpentry & Joinery

Hello, I would like a flyer designed for my new business doing small projects in my local area for home-owners. I am a professional tradesman.
The type of work I am offering is:
- decks/decking
- external stairs & railings
- install windows & doors
- roofs & gutters
- small additions
- built-in wardrobes
- finish work
- demolition

It would be great if the flyer could mention these, or use phrasing that fits this kind of construction work.
My idea for a slogan was "new work and repairs to any age home".

Please also mention FREE QUOTES and have my email and phone number included on the flyer, along with my carpentry licence number, which I can provided.

I'd like a one page, single-sided flyer that could be printed as DL.
Colour and style is up to you! I'll be placing this flyer on counters & in the windows of local businesses, so something simple and eye-catching is preferred.

Thank you!

```html
<!DOCTYPE html>
<html lang="en">
<head>
<meta charset="utf-8">
<title>Marcus Pellow Carpentry &amp; Joinery</title>
<link href="https://fonts.googleapis.com/css2?family=Open+Sans:wght@600;700;800&family=Roboto:wght@300;400;500;700&display=swap" rel="stylesheet">
<style>
  :root {
    --brown: #5a4f48;
    --brown-dark: #4a403a;
    --stone: #bdbbb9;
    --bubble: #e6e4e2;
    --white: #ffffff;
    --tagline: #cfcac6;
    --wood-light: #d8b994;
    --wood-mid: #a98461;
  }
  * { margin: 0; padding: 0; box-sizing: border-box; }
  html, body { width: 851px; height: 1200px; overflow: hidden; background: var(--brown); }
  .flyer { position: relative; width: 851px; height: 1200px; overflow: hidden; font-family: "Roboto", sans-serif; }

  .masthead { position: absolute; left: 0; top: 0; width: 851px; height: 301px; background: var(--brown); }
  .brand-frame {
    position: absolute; left: 129px; top: 29px; width: 567px; height: 139px;
    border: 3px solid var(--white); text-align: center; color: var(--white);
    font-family: "Open Sans", sans-serif; font-weight: 700;
  }
  .brand-name { display: block; font-size: 54px; letter-spacing: 3px; line-height: 1; margin-top: 14px; text-shadow: 0 2px 3px rgba(0,0,0,.35); }
  .brand-trade { display: block; font-size: 36px; letter-spacing: 2px; line-height: 1; margin-top: 14px; text-shadow: 0 2px 3px rgba(0,0,0,.35); }
  .tagline { position: absolute; left: 0; top: 196px; width: 851px; text-align: center; color: var(--tagline); font-size: 25px; font-weight: 400; letter-spacing: 2.5px; }

  .services { position: absolute; left: 0; top: 301px; width: 851px; height: 318px; display: grid; grid-template-columns: repeat(4, 1fr); grid-template-rows: repeat(2, 1fr); gap: 2px; background: var(--white); }
  .service { position: relative; display: flex; align-items: center; justify-content: center; }
  .service-label { position: relative; color: var(--white); font-family: "Open Sans", sans-serif; font-weight: 600; font-size: 25px; letter-spacing: 2px; text-shadow: 0 1px 4px rgba(0,0,0,.8); }
  .service-label.small { font-size: 16px; letter-spacing: 1px; }
  .svc-decking { background: linear-gradient(180deg, #6f8a55 0%, #8a6a48 100%); }
  .svc-stairs { background: linear-gradient(180deg, #e3cf96 0%, #c9a06a 100%); }
  .svc-windows { background: linear-gradient(180deg, #a3685a 0%, #8a5444 100%); }
  .svc-roofs { background: linear-gradient(180deg, #8f98a4 0%, #a46a55 100%); }
  .svc-additions { background: linear-gradient(180deg, #8da2b8 0%, #9c7660 100%); }
  .svc-wardrobes { background: linear-gradient(180deg, #c7a678 0%, #a77e50 100%); }
  .svc-finish { background: linear-gradient(180deg, #6b7b56 0%, #4f6340 100%); }
  .svc-demolition { background: linear-gradient(180deg, #a9aab0 0%, #7a6150 100%); }

  .offer-band { position: absolute; left: 0; top: 619px; width: 851px; height: 188px; background: var(--stone); }
  .offer { position: absolute; left: 0; top: 46px; width: 851px; text-align: center; color: var(--brown); font-family: "Roboto", sans-serif; font-weight: 700; font-size: 98px; letter-spacing: 12px; line-height: 1; }

  .contact-area { position: absolute; left: 0; top: 807px; width: 851px; height: 393px; background: linear-gradient(180deg, var(--brown) 0%, var(--brown-dark) 28%, var(--wood-mid) 70%, var(--wood-light) 100%); }
  .workshop-photo { position: absolute; left: 0; top: 120px; width: 851px; height: 273px; background: linear-gradient(180deg, rgba(90,79,72,0) 0%, rgba(216,185,148,.55) 60%, rgba(230,205,170,.8) 100%); }

  .contact { position: absolute; top: 780px; width: 300px; margin-left: -150px; text-align: center; }
  .contact-icon { display: block; margin: 0 auto; width: 96px; height: 106px; }
  .contact-text { display: block; margin-top: 14px; color: var(--white); font-size: 12px; letter-spacing: .5px; }
  .contact-email { left: 144px; }
  .contact-phone { left: 427px; }
  .contact-licence { left: 716px; }
</style>
</head>
<body>
<main class="flyer">
  <header class="masthead">
    <h1 class="brand-frame">
      <span class="brand-name">MARCUS PELLOW</span>
      <span class="brand-trade">CARPENTRY &amp; JOINERY</span>
    </h1>
    <p class="tagline">NEW WORK AND REPAIRS TO ANY AGE HOME</p>
  </header>

  <section class="services">
    <div class="service svc-decking" role="img" aria-label="Photo of a timber deck with steps in a garden"><span class="service-label">DECKING</span></div>
    <div class="service svc-stairs" role="img" aria-label="Photo of a staircase with iron railing"><span class="service-label">STAIRS</span></div>
    <div class="service svc-windows" role="img" aria-label="Photo of a brick house with bay windows and doors"><span class="service-label small">WINDOWS/DOORS</span></div>
    <div class="service svc-roofs" role="img" aria-label="Photo of a tiled roof with gutters"><span class="service-label small">ROOFS/GUTTERS</span></div>
    <div class="service svc-additions" role="img" aria-label="Photo of a home addition with veranda"><span class="service-label">ADDITIONS</span></div>
    <div class="service svc-wardrobes" role="img" aria-label="Photo of built-in timber wardrobes"><span class="service-label">WARDROBES</span></div>
    <div class="service svc-finish" role="img" aria-label="Photo of a finished white cottage among trees"><span class="service-label">FINISH WORK</span></div>
    <div class="service svc-demolition" role="img" aria-label="Photo of a demolition site with an excavator"><span class="service-label">DEMOLITION</span></div>
  </section>

  <section class="offer-band">
    <h2 class="offer">FREE QUOTES</h2>
  </section>

  <section class="contact-area">
    <div class="workshop-photo" role="img" aria-label="Photo of a carpenter drilling into timber boards on a workbench"></div>
  </section>

  <div class="contact contact-email">
    <svg class="contact-icon" viewBox="0 0 96 106" aria-hidden="true">
      <path d="M48 106 L36 90 A47 47 0 1 1 60 90 Z" fill="var(--bubble)"/>
      <rect x="28" y="34" width="40" height="28" fill="var(--brown)"/>
      <path d="M28 34 L48 52 L68 34" fill="none" stroke="var(--bubble)" stroke-width="3"/>
    </svg>
    <span class="contact-text">MARCUSPELLOW15@TRADESMAIL.COM</span>
  </div>
  <div class="contact contact-phone">
    <svg class="contact-icon" viewBox="0 0 96 106" aria-hidden="true">
      <path d="M48 106 L36 90 A47 47 0 1 1 60 90 Z" fill="var(--bubble)"/>
      <rect x="35" y="22" width="26" height="48" rx="4" fill="var(--brown)"/>
      <rect x="39" y="28" width="18" height="28" fill="var(--bubble)"/>
      <circle cx="48" cy="63" r="3" fill="var(--bubble)"/>
    </svg>
    <span class="contact-text">0491 570 156</span>
  </div>
  <div class="contact contact-licence">
    <svg class="contact-icon" viewBox="0 0 96 106" aria-hidden="true">
      <path d="M48 106 L36 90 A47 47 0 1 1 60 90 Z" fill="var(--bubble)"/>
      <circle cx="48" cy="36" r="11" fill="var(--brown)"/>
      <path d="M26 70 Q26 50 48 50 Q70 50 70 70 Z" fill="var(--brown)"/>
    </svg>
    <span class="contact-text">HTLB LICENCE NUMBER: 1048375</span>
  </div>
</main>
</body>
</html>
```